RT Penbrook, LLC Business Card

I want a two-sided business card that provides people with our contact information, our mission, and a sample of our services. I would love a QR code somewhere on the card linking to our website if possible (www.rtpenbrookco.example).
Mission:
To help social service organizations develop a Mission Aligned Data Driven mindset that promotes positive change in the lives of the customers they serve.
Services:
Consulting
Training
Community Assessment Development
Strategic Planning
Report Development
Data Analytics
(Note: the website domain is currently mid-transfer so you can't see it at the link we want on the card. You can, however, view it for reference at https://rtpenbrookco.blogsite.example/)
Contact Information for Business Card
Name: Derek Penbrook, NCRT/MT
Title: Chief Executive Officer
Address: 4178 Larch Lane, Cumming, Georgia 30041
Telephone: (706) 555-0184
Email: derek@rtpenbrookco.example
Colors
Designer to choose colors to be used in the design.
Look and feel

```html
<!DOCTYPE html>
<html lang="en">
<head>
<meta charset="utf-8">
<title>RT Penbrook, LLC Business Card</title>
<link href="https://fonts.googleapis.com/css2?family=Roboto:wght@400;500;700&display=swap" rel="stylesheet">
<style>
  :root {
    --brand-blue: #35a5d8;
    --charcoal: #4a4a4f;
    --white: #ffffff;
    --page: #e6e6e6;
    --ink-light: #e9e9ec;
  }
  * { box-sizing: border-box; margin: 0; padding: 0; }
  html, body {
    width: 1200px; height: 1200px; overflow: hidden;
    background: var(--page);
    font-family: 'Roboto', Arial, sans-serif;
  }
  .sheet {
    width: 1200px; height: 1200px;
    display: flex; flex-direction: column; align-items: center; justify-content: center;
    gap: 60px;
  }
  .card {
    width: 875px; height: 500px; border-radius: 32px; overflow: hidden;
    position: relative;
    box-shadow: 0 10px 30px rgba(0,0,0,0.18);
  }
  .card-front {
    background: var(--brand-blue);
    display: flex; align-items: center; justify-content: center;
  }
  .wordmark {
    display: flex; align-items: center; gap: 22px;
    font-weight: 700; color: var(--white);
    font-size: 64px; letter-spacing: 1px;
    white-space: nowrap;
  }
  .wordmark-dot {
    width: 70px; height: 70px; border-radius: 50%;
    background: var(--white); flex: none;
  }
  .card-back { background: var(--white); }
  .back-brand {
    position: absolute; left: 0; right: 0; top: 0; height: 48%;
    display: flex; align-items: center; justify-content: center;
  }
  .back-brand .wordmark { color: var(--charcoal); font-size: 58px; }
  .back-brand .wordmark-dot { background: var(--brand-blue); width: 64px; height: 64px; }
  .info-band {
    position: absolute; left: 0; right: 0; bottom: 0; height: 52%;
    background: var(--charcoal);
    display: flex; justify-content: space-between;
    padding: 36px 60px 30px 70px;
    color: var(--white);
  }
  .contact .person-name { color: var(--brand-blue); font-weight: 700; font-size: 25px; white-space: nowrap; }
  .contact .person-title { font-weight: 700; font-size: 17px; margin-top: 2px; }
  .contact .address { font-size: 16px; line-height: 1.3; margin-top: 18px; color: var(--ink-light); }
  .contact-lines { list-style: none; margin-top: 8px; }
  .contact-lines li {
    display: flex; align-items: center; gap: 10px;
    font-size: 16px; line-height: 1.55; color: var(--ink-light);
    white-space: nowrap;
  }
  .contact-lines svg { width: 18px; height: 18px; flex: none; }
  .accent { color: var(--brand-blue); }
  .services { list-style: none; padding-top: 4px; }
  .services li {
    display: flex; align-items: center; gap: 10px;
    font-size: 16px; font-weight: 500; line-height: 1.9;
    white-space: nowrap;
  }
  .services li::before {
    content: ""; width: 7px; height: 7px; background: var(--brand-blue); flex: none;
  }
</style>
</head>
<body>
<main class="sheet">
  <section class="card card-front" aria-label="Card front">
    <div class="wordmark"><span class="wordmark-dot"></span><span>RT Penbrook, LLC</span></div>
  </section>

  <section class="card card-back" aria-label="Card back">
    <div class="back-brand">
      <div class="wordmark"><span class="wordmark-dot"></span><span>RT Penbrook, LLC</span></div>
    </div>
    <div class="info-band">
      <div class="contact">
        <p class="person-name">Derek Penbrook, NCRT/MT</p>
        <p class="person-title">Chief Executive Officer</p>
        <p class="address">4178 Larch Lane, Cumming,<br>Georgia 30041</p>
        <ul class="contact-lines">
          <li>
            <svg viewBox="0 0 20 20" aria-hidden="true"><circle cx="10" cy="10" r="8.5" fill="none" stroke="#35a5d8" stroke-width="1.5"/><path d="M7 5.5l1.6 0 .8 2.2-1 .9a6 6 0 0 0 2.9 2.9l.9-1 2.2.8v1.6c0 .5-.4.9-.9.9A7.6 7.6 0 0 1 6.1 6.4c0-.5.4-.9.9-.9z" fill="#35a5d8"/></svg>
            (706) 555-0184
          </li>
          <li>
            <svg viewBox="0 0 20 20" aria-hidden="true"><circle cx="10" cy="10" r="8.5" fill="none" stroke="#35a5d8" stroke-width="1.5"/><rect x="5.5" y="7" width="9" height="6.5" fill="none" stroke="#35a5d8" stroke-width="1.2"/><path d="M5.5 7l4.5 3.6L14.5 7" fill="none" stroke="#35a5d8" stroke-width="1.2"/></svg>
            derek@rtpenbrookco.example
          </li>
          <li>
            <svg viewBox="0 0 20 20" aria-hidden="true"><circle cx="10" cy="10" r="8.5" fill="none" stroke="#35a5d8" stroke-width="1.5"/><circle cx="10" cy="10" r="4.5" fill="none" stroke="#35a5d8" stroke-width="1.1"/><path d="M5.5 10h9M10 5.5c-2 2.5-2 6.5 0 9M10 5.5c2 2.5 2 6.5 0 9" fill="none" stroke="#35a5d8" stroke-width="1"/></svg>
            <span>www.<span class="accent">rtpenbrookco</span>.example</span>
          </li>
        </ul>
      </div>
      <ul class="services">
        <li>Consulting</li>
        <li>Training</li>
        <li>Community Assessment Development</li>
        <li>Strategic Planning</li>
        <li>Report Development</li>
        <li>Data Analytics</li>
      </ul>
    </div>
  </section>
</main>
</body>
</html>
```